Graphic Design Project

Hi,

I would like to create a beer label for our new beer we are creating,

We are called "The Marrowfield Brewing Co."

Our new beer is called "The Wandering Lamplighter" which is a "Pale Ale" with an "ABV 4.8%"

our tag line is "Built For Sessionability"

Everything writen in inverted comma's I would like on the label

I would like it to be a round beer label as well with some sort of picture in the background.

This is our first design of any kind for the company so we do not have a logo or any designs so its open to anything. I would like it to be new and trendy with an older style feel to it.

Industry/Entity Type

Graphic Design

Requirements
Must have
• Round so I can convert into a beer coaster,
needs to have alcohol percentage.

```html
<!DOCTYPE html>
<html lang="en">
<head>
<meta charset="utf-8">
<title>The Wandering Lamplighter – Pale Ale Label</title>
<link href="https://fonts.googleapis.com/css2?family=Bebas+Neue&family=Montserrat:wght@500;600&display=swap" rel="stylesheet">
<style>
  :root {
    --label-brown: #523f28;
    --band-gold: #f0c766;
    --centre-green: #607333;
    --wheat-tone: #8c7b63;
    --ink-white: #ffffff;
    --page: #ffffff;
  }
  html, body {
    margin: 0;
    padding: 0;
    width: 1200px;
    height: 900px;
    overflow: hidden;
    background: var(--page);
  }
  .canvas {
    position: relative;
    width: 1200px;
    height: 900px;
  }
  .label-art {
    position: absolute;
    inset: 0;
  }
  .ring-text {
    font-family: "Montserrat", sans-serif;
    font-weight: 600;
    fill: var(--band-gold);
  }
  .ring-text--brewery { font-size: 32px; letter-spacing: 0.06em; }
  .ring-text--tagline { font-size: 40px; letter-spacing: 0.12em; }
  .centre-copy {
    position: absolute;
    inset: 0;
  }
  .centre-copy > * {
    position: absolute;
    left: 0;
    width: 1200px;
    margin: 0;
    text-align: center;
    white-space: nowrap;
  }
  .beer-name {
    top: 340px;
    font-family: "Bebas Neue", sans-serif;
    font-weight: 400;
    font-size: 52px;
    line-height: 1;
    color: var(--ink-white);
  }
  .beer-style {
    top: 387px;
    font-family: "Bebas Neue", sans-serif;
    font-weight: 400;
    font-size: 156px;
    line-height: 1;
    color: var(--band-gold);
  }
  .beer-abv {
    top: 566px;
    font-family: "Montserrat", sans-serif;
    font-weight: 500;
    font-size: 19px;
    line-height: 1.2;
    letter-spacing: 0.08em;
    color: var(--ink-white);
  }
</style>
</head>
<body>
<main class="canvas">
  <svg class="label-art" width="1200" height="900" viewBox="0 0 1200 900" xmlns="http://www.w3.org/2000/svg">
    <defs>
      <clipPath id="label-disc">
        <circle cx="600" cy="450" r="437"/>
      </clipPath>
      <path id="arc-top" d="M 228 450 A 372 372 0 0 1 972 450"/>
      <path id="arc-bottom" d="M 215 450 A 385 385 0 0 0 985 450"/>
    </defs>

    <g clip-path="url(#label-disc)">
      <circle class="label-base" cx="600" cy="450" r="437" fill="var(--label-brown)"/>
      <circle class="wheat-wreath" role="img" aria-label="Wreath of wheat ears circling the centre badge"
              cx="600" cy="440" r="305" fill="none" stroke="var(--wheat-tone)" stroke-width="80" opacity="0.85"/>
      <rect class="gold-band" x="150" y="293" width="900" height="315" fill="var(--band-gold)"/>
    </g>

    <circle class="centre-badge" cx="600" cy="440" r="262" fill="var(--centre-green)"/>

    <text class="ring-text ring-text--brewery">
      <textPath href="#arc-top" startOffset="50%" text-anchor="middle" textLength="740" lengthAdjust="spacing">THE MARROWFIELD BREWING COMPANY</textPath>
    </text>
    <text class="ring-text ring-text--tagline">
      <textPath href="#arc-bottom" startOffset="50%" text-anchor="middle">BUILT FOR SESSIONABILITY</textPath>
    </text>
  </svg>

  <section class="centre-copy">
    <h1 class="beer-name">THE WANDERING LAMPLIGHTER</h1>
    <p class="beer-style">PALE ALE</p>
    <p class="beer-abv">ABV 4.8%</p>
  </section>
</main>
</body>
</html>
```